Harbor Business Cards

I need a business card designed with the following information.

Company Name: Harbor Wealth Management
Name: BriAnne Dockery
Title: Executive Assistant
Cell: (281) 555-0173
Direct Line: (832) 555-0148
Email: brianne@harborwmx.com
Address: 20537 W. Marlowe PKWY Ste. B
Tomball, TX 77390

I have attached the logo.
I would like it in navy blue and silver.
Thanks.

```html
<!DOCTYPE html>
<html lang="en">
<head>
<meta charset="utf-8">
<title>Harbor Wealth Management — Business Card</title>
<link href="https://fonts.googleapis.com/css2?family=Open+Sans:wght@400;600&family=Arimo:wght@400;500&display=swap" rel="stylesheet">
<style>
  :root {
    --page: #ffffff;
    --navy: #2c3549;
    --navy-band-top: #343d52;
    --navy-band-bottom: #59627a;
    --emblem-light: #535c73;
    --silver: #cfd0d3;
    --white: #ffffff;
  }
  html, body {
    margin: 0;
    padding: 0;
    width: 1200px;
    height: 1200px;
    overflow: hidden;
    background: var(--page);
  }
  .card {
    position: absolute;
    left: 271px;
    width: 659px;
    height: 378px;
    background: var(--navy);
    overflow: hidden;
  }
  .card--front { top: 212px; }
  .card--back { top: 611px; }
  .card__art {
    position: absolute;
    inset: 0;
    width: 659px;
    height: 378px;
  }
  .card--back .card__art { transform: scaleX(-1); }
  .identity {
    position: absolute;
    width: 310px;
    text-align: center;
  }
  .card--front .identity { left: 334px; top: 48px; }
  .card--back .identity { left: 15px; top: 48px; }
  .identity__name {
    font-family: "Open Sans", sans-serif;
    font-weight: 600;
    font-size: 37px;
    line-height: 52px;
    white-space: nowrap;
    color: var(--silver);
    margin: 0;
  }
  .identity__rule {
    height: 2px;
    background: var(--silver);
    margin: 6px 0 0;
  }
  .identity__title {
    font-family: "Open Sans", sans-serif;
    font-weight: 400;
    font-size: 19px;
    line-height: 26px;
    letter-spacing: 4.1px;
    white-space: nowrap;
    color: var(--silver);
    margin: 1px 0 0;
  }
  .contact {
    position: absolute;
    font-family: "Arimo", sans-serif;
    color: var(--white);
    white-space: nowrap;
  }
  .card--front .contact { left: 341px; top: 228px; }
  .card--back .contact { left: 22px; top: 228px; }
  .contact__row {
    display: flex;
    align-items: center;
    gap: 6px;
    font-size: 14.5px;
    font-weight: 500;
    height: 22px;
    margin-bottom: 10px;
  }
  .contact__icon { width: 18px; height: 18px; flex: none; }
  .contact__address {
    font-size: 12.5px;
    font-weight: 500;
    margin-left: 1px;
    margin-top: -1px;
  }
</style>
</head>
<body>

<section class="card card--front">
  <svg class="card__art" viewBox="0 0 659 378">
    <defs>
      <linearGradient id="band-front" x1="0" y1="0" x2="0" y2="1">
        <stop offset="0" stop-color="var(--navy-band-top)"/>
        <stop offset="1" stop-color="var(--navy-band-bottom)"/>
      </linearGradient>
      <linearGradient id="emblem-front" x1="0" y1="0" x2="0" y2="1">
        <stop offset="0" stop-color="var(--navy)" stop-opacity="0"/>
        <stop offset="1" stop-color="var(--emblem-light)" stop-opacity="0.6"/>
      </linearGradient>
    </defs>
    <rect role="img" aria-label="Faint brand emblem decoration" x="0" y="80" width="180" height="235" fill="url(#emblem-front)"/>
    <rect x="0" y="315" width="659" height="49" fill="url(#band-front)"/>
    <rect x="0" y="364" width="659" height="1.5" fill="var(--white)"/>
  </svg>
  <div class="identity">
    <h1 class="identity__name">BriAnne Dockery</h1>
    <div class="identity__rule"></div>
    <p class="identity__title">Executive Assistant</p>
  </div>
  <div class="contact">
    <div class="contact__row">
      <svg class="contact__icon" viewBox="0 0 18 18"><circle cx="9" cy="9" r="8" fill="none" stroke="#fff" stroke-width="1.3"/><path d="M6 4.6c.5-.3 1-.2 1.2.2l.8 1.6c.2.4 0 .8-.3 1l-.6.4c.4 1.1 1.1 2 2.1 2.6l.5-.5c.3-.3.8-.3 1.1-.1l1.4 1c.4.3.4.8.1 1.2l-.6.6c-.6.6-2 .4-3.5-.8-1.6-1.3-2.7-3.2-2.7-4.8 0-.7.2-1.2.5-1.4z" fill="#fff"/></svg>
      <span>(281) 555 - 0173 - (832) 555 - 0148</span>
    </div>
    <div class="contact__row">
      <svg class="contact__icon" viewBox="0 0 18 18"><text x="9" y="14.5" text-anchor="middle" font-family="Arimo, sans-serif" font-size="18" fill="#fff">@</text></svg>
      <span>brianne@harborwmx.com</span>
    </div>
    <div class="contact__address">20537 W. Marlowe PKWY Ste. B Tomball, TX 77390</div>
  </div>
</section>

<section class="card card--back">
  <svg class="card__art" viewBox="0 0 659 378">
    <defs>
      <linearGradient id="band-back" x1="0" y1="0" x2="0" y2="1">
        <stop offset="0" stop-color="var(--navy-band-top)"/>
        <stop offset="1" stop-color="var(--navy-band-bottom)"/>
      </linearGradient>
      <linearGradient id="emblem-back" x1="0" y1="0" x2="0" y2="1">
        <stop offset="0" stop-color="var(--navy)" stop-opacity="0"/>
        <stop offset="1" stop-color="var(--emblem-light)" stop-opacity="0.6"/>
      </linearGradient>
    </defs>
    <rect role="img" aria-label="Faint brand emblem decoration" x="0" y="80" width="180" height="235" fill="url(#emblem-back)"/>
    <rect x="0" y="315" width="659" height="49" fill="url(#band-back)"/>
    <rect x="0" y="364" width="659" height="1.5" fill="var(--white)"/>
  </svg>
  <div class="identity">
    <h2 class="identity__name">BriAnne Dockery</h2>
    <div class="identity__rule"></div>
    <p class="identity__title">Executive Assistant</p>
  </div>
  <div class="contact">
    <div class="contact__row">
      <svg class="contact__icon" viewBox="0 0 18 18"><circle cx="9" cy="9" r="8" fill="none" stroke="#fff" stroke-width="1.3"/><path d="M6 4.6c.5-.3 1-.2 1.2.2l.8 1.6c.2.4 0 .8-.3 1l-.6.4c.4 1.1 1.1 2 2.1 2.6l.5-.5c.3-.3.8-.3 1.1-.1l1.4 1c.4.3.4.8.1 1.2l-.6.6c-.6.6-2 .4-3.5-.8-1.6-1.3-2.7-3.2-2.7-4.8 0-.7.2-1.2.5-1.4z" fill="#fff"/></svg>
      <span>(281) 555 - 0173 - (832) 555 - 0148</span>
    </div>
    <div class="contact__row">
      <svg class="contact__icon" viewBox="0 0 18 18"><text x="9" y="14.5" text-anchor="middle" font-family="Arimo, sans-serif" font-size="18" fill="#fff">@</text></svg>
      <span>brianne@harborwmx.com</span>
    </div>
    <div class="contact__address">20537 W. Marlowe PKWY Ste. B Tomball, TX 77390</div>
  </div>
</section>

</body>
</html>
```